Australia-Wide Industry Leader Bookkeeping Business Website Design Required

We need a website designed for our 10 year old bookkeeping business, Linden & Crane. Linden & Crane has been servicing the local & interstate communities of Australia, providing first-class BAS & Bookkeeping services with a personal touch unmatched by anyone else in the county.

What began 10 years ago as a small business focusing on family, friends and the local community, it has since grown into a well respected business with 95% of their business based solely on word of mouth and personal referrals from around Australia.

We would like to see designs that incorporate our existing brand/logo. The colours to be used on the website should be colours that work well with our logo. The design should communicate maturity, trust and confidence with a Web 2.0 look and feel.

We have produced mockups of the entire website as well as assets used in the mockups. Please reference the attached files. The mockups are an example of all the design elements that we want on each page. Designers are encouraged to use the mockups as a guideline only and for designers to use their own creativity.
Updates

This message is for new graphic designers who are considering commencing work on this project. Thank you for expressing an interest in our project. We would like to inform you that this project is close to completion as we have a number designs under very serious consideration.

We are currently in a position where we are disinterested providing feedback to improve on new designs submitted. We will provide feedback to improve new designs only if the submitted designs are very close to what we want for our website, and will only require 1 or 2 revision rounds to refine before the project completion date we will not work with designers to refine their newly submitted designs.

We feel that it is important for all designers to know the above information as we feel that your time and effort may be better spent working on another project.

Thank you for your understanding.

A big thank you for all the designs submitted. We are now in the process of selecting a design. Please be patient during this process. Thank you.

Target Market(s)

Busy Business Owners

Industry/Entity Type

Small Business

Requirements
Must have
• We require a rectangular "slide show" type feature to serve as a "teaser" to arouse the emotions of our website visitors. Each slide asks a specific question. The questions are:

- Is your paperwork in a mess?
- Do you need to get organised for the end of financial year?
- Are you sick & tired of endless amounts of paperwork & BASs?
- Do you feel frustrated & annoyed because you know your books need to be done?
- Do you lack the time & patience to get your paperwork done?
- Do you wish you had more time to do the things you enjoy doing?
- Contact Linden & Crane today and we will transform your chaos into order.

Underneath the slide show will be a button to "Call Linden & Crane Now - 03 7482 9163".

```html
<!DOCTYPE html>
<html lang="en">
<head>
<meta charset="utf-8">
<title>Linden &amp; Crane – BAS &amp; Bookkeeping</title>
<link href="https://fonts.googleapis.com/css2?family=PT+Sans:wght@400;700&family=Open+Sans:wght@300;400&display=swap" rel="stylesheet">
<style>
:root{
  --brand:#9b0d12;
  --brand-dark:#7a0a0e;
  --ink:#2a2a2a;
  --text:#555;
  --tick:#7cb342;
  --page:#e6e6e6;
  --card:#ffffff;
  --footer:#9c9c9c;
}
*{margin:0;padding:0;box-sizing:border-box}
html,body{width:816px;height:1200px;overflow:hidden}
body{position:relative;font-family:"PT Sans",sans-serif;color:var(--text);background:var(--page)}
.abs{position:absolute}
.topline{left:0;top:0;width:816px;height:4px;background:var(--brand)}
.header{left:0;top:4px;width:816px;height:142px;background:linear-gradient(#dedede,#fafafa 60%,#fff);border-bottom:1px solid #d0d0d0}
.wordmark{left:76px;top:29px;width:206px;height:40px;background:#fff;border:1px solid #333;display:flex;align-items:center;gap:8px;padding-left:10px;font-size:20px;font-weight:700;color:var(--brand)}
.wordmark i{width:14px;height:14px;background:var(--brand);display:block}
.nav{left:324px;top:41px;display:flex;gap:4px;font-size:9.5px;color:#222}
.nav a{padding:4px 8px;color:inherit;text-decoration:none}
.nav a.active{background:var(--brand);color:#fff;border-radius:2px}
.intro{left:75px;top:95px;width:680px;font-size:12px;line-height:16px;color:#222}
.hero{left:0;top:146px;width:816px;height:261px;background:linear-gradient(#f3f3f3,#fff 50%,#eee);border-bottom:1px solid #ccc}
.hero h2{position:absolute;left:80px;top:78px;font-size:21px;color:var(--brand);font-weight:700}
.callbtn{position:absolute;left:78px;top:120px;width:130px;height:32px;border-radius:16px;background:linear-gradient(#fff,#dbe8f1);box-shadow:0 0 0 2px #e8eef3,0 1px 3px #999;font-size:12.5px;color:#222;display:flex;align-items:center;padding-left:12px;gap:30px}
.callbtn svg{width:15px;height:15px}
.photo{position:absolute;left:400px;top:4px;width:380px;height:252px;background:radial-gradient(ellipse at 60% 50%,#c9b8a2,#e8e2da 55%,#f5f5f5 80%)}
.dots{position:absolute;left:88px;top:246px;display:flex;gap:3px}
.dots b{width:8px;height:8px;border-radius:50%;background:#111}
.dots b:first-child{background:#c8151b}
.welcome{left:75px;top:430px;font-family:"Open Sans",sans-serif;font-weight:300;font-size:22px;color:#222}
.welcome strong{font-family:"PT Sans",sans-serif;font-weight:700;color:var(--brand)}
.about{left:75px;top:462px;width:662px;font-size:9.2px;line-height:13.6px;letter-spacing:.1px}
.card{background:var(--card);border:1px solid #d6d6d6;border-radius:4px}
.tab{height:24px;background:var(--brand);color:#fff;font-size:12px;display:flex;align-items:center;padding-left:22px;border-radius:0 4px 4px 0;box-shadow:0 2px 3px rgba(0,0,0,.3);white-space:nowrap;overflow:hidden}
.tab.long{font-size:11px;padding-left:16px}
.tick{display:flex;align-items:flex-start;gap:6px}
.tick::before{content:"";flex:none;width:10px;height:8px;margin-top:1px;background:var(--tick);clip-path:polygon(0 55%,18% 38%,40% 62%,84% 0,100% 15%,40% 100%)}
.list{font-size:8.4px;color:#444;line-height:15.6px}
.sub{font-size:8.4px;color:#444;line-height:14.4px;list-style:none}
.sub li::before{content:"• ";color:var(--tick)}
.red{color:#c00;font-size:9.5px}
.map{left:518px;top:668px;width:204px;height:191px;background:radial-gradient(ellipse at 50% 50%,#8fc751,#bde08d 55%,#f4f9ee 75%)}
.qual{font-size:9px;color:#333;line-height:24px}
.band{left:0;top:1086px;width:816px;height:76px;background:linear-gradient(#fff,#eee)}
.badge{position:absolute;top:8px;height:60px;border-radius:3px}
.footer{left:0;top:1162px;width:816px;height:38px;background:var(--footer);color:#fff;font-size:8.5px;display:flex;align-items:center;justify-content:center}
.social{position:absolute;top:10px;width:18px;height:18px;border-radius:3px}
</style>
</head>
<body>
<div class="abs topline"></div>
<header class="abs header"></header>
<div class="abs wordmark"><i></i>Linden &amp; Crane</div>
<nav class="abs nav">
  <a class="active">Home</a><a>About Us</a><a>Services</a><a>Testimonials</a><a>Articles</a><a>Endorsements</a><a>Links</a><a>Contact Us</a>
</nav>
<p class="abs intro">For nearly 10 years Linden &amp; Crane has been servicing the local &amp; interstate communities of Australia, providing first-class BAS &amp; Bookkeeping services with a personal touch unmatched by anyone else in the country</p>

<section class="abs hero">
  <div class="photo" role="img" aria-label="Photo of a stressed office worker beside a tall stack of folders and paperwork"></div>
  <h2>Is your paperwork in a mess?</h2>
  <div class="callbtn">Call us today
    <svg viewBox="0 0 16 16"><circle cx="8" cy="8" r="8" fill="#9b0d12"/><path d="M4 8h6M8 5l3 3-3 3" stroke="#fff" stroke-width="2" fill="none"/></svg>
  </div>
  <div class="dots"><b></b><b></b><b></b><b></b><b></b></div>
</section>

<h1 class="abs welcome">Welcome to <strong>Linden &amp; Crane</strong></h1>
<p class="abs about">Having worked for a Certified Accountants firm for numerous years, Helen Linden &amp; Clare Crane become concerned about the consistency of inaccurate books prepared by others in various organisations. As the quality of bookwork declined. The fees seemed to increase. Together they identified a need for a quality bookkeeping service that truly understood what being in business is all about and more importantly.how to correctly &amp; accurately process books according to the laws and requirments set by Australina Taxation office. They wanted to give people a better alternative- thus Linden &amp; Crane was born. What began as a samll busines focusing on family. Friends and the local community has since grown into a well respected business with 95% of their business based solely on word of mouth and personal referrals from around Australia</p>

<div class="abs card" style="left:79px;top:570px;width:396px;height:498px"></div>
<div class="abs tab" style="left:66px;top:575px;width:181px">To Summarise</div>
<div class="abs list" style="left:87px;top:606px">
  <div class="tick">Free initial consultation</div><div class="tick">Registered BAS Agent #41826-217</div><div class="tick">Bookkeeping</div><div class="tick">BAS Preparation &amp; Logdgement</div><div class="tick">Payroll</div><div class="tick">IAS Preparation &amp; Logdgement</div>
</div>
<div class="abs list" style="left:290px;top:606px">
  <div class="tick">Superannuation &amp; Workcover</div><div class="tick">Margin Scheme</div><div class="tick">Fuel Tax Credits</div><div class="tick">Offsite &amp; onsite bookkeeping</div><div class="tick">LedgerBooks Software &amp; Training</div><div class="tick">Australia wide</div>
</div>
<p class="abs red" style="left:89px;top:713px">What makes Linden &amp; Crane different from other Bookkeepers</p>
<div class="abs list" style="left:87px;top:738px;width:320px">
  <div class="tick">We guarantee the quality of our work</div><div class="tick">We have ovaer 35 years of experieence</div><div class="tick">We have owned &amp; operated businesses for 35 years</div><div class="tick">The Linden &amp; Crane team are investors &amp; traders</div><div class="tick">Extensive business network for your benefit</div><div class="tick">Backed by a team of accountants</div>
  <div class="tick" style="line-height:13.6px;margin-top:2px">We work with a team of elite accointants &amp; wealth creation professionals who coach us monthly in the following:</div>
</div>
<ul class="abs sub" style="left:115px;top:873px"><li>Asset Protection</li><li>Superannuation &amp; Self Managed Superannuation Funds</li><li>Property Investing</li><li>Tax strategies. tax structures &amp; best tax savings</li></ul>
<div class="abs tick red" style="left:87px;top:938px;width:380px;line-height:13.6px">We understand just how important it is to help lead &amp; guide our clients from making profits to:</div>
<ul class="abs sub" style="left:115px;top:981px"><li>Maximising profits</li><li>Wealth creation</li><li>Tax Minimisation</li><li>Asset protection</li></ul>
<p class="abs red" style="left:88px;top:1046px">This is something that other bookkeepers just dont do!</p>

<div class="abs card" style="left:508px;top:572px;width:233px;height:496px"></div>
<div class="abs tab" style="left:494px;top:578px;width:182px">Servicing All of Australia</div>
<p class="abs" style="left:517px;top:615px;width:216px;font-size:8px;line-height:13.6px;color:#666">95% of our clients come from client &amp; accountant referrals. We have clients all over Victoria. Queensland, NSW &amp; Western Australia so no matter where you are we can help</p>
<div class="abs map" role="img" aria-label="Map of Australia marking major cities served"></div>
<div class="abs tab long" style="left:494px;top:863px;width:236px">Qualifiactions, Memberships and Partnerships</div>
<div class="abs qual" style="left:517px;top:896px">
  <div class="tick">Registered ATO BAS Agent</div><div class="tick">Certificate IV Financial Services</div><div class="tick">Certificate III Financial Services</div><div class="tick">Member of Guild of Chartered Bookkeepers</div><div class="tick">Platium Member of Allied Bookkeepers</div><div class="tick">Tallyline Professional Partner</div><div class="tick">Tax Clever Australia</div>
</div>

<div class="abs band">
  <div class="badge" style="left:118px;width:58px;background:#c9a9a9"></div>
  <div class="badge" style="left:242px;width:72px;background:#e2b49a"></div>
  <div class="badge" style="left:371px;width:36px;background:#2b4a7a"></div>
  <div class="badge" style="left:472px;width:34px;background:#b8b8b8"></div>
  <div class="badge" style="left:570px;width:140px;height:30px;top:22px;background:#c6c6c6"></div>
</div>
<footer class="abs footer">
  <span class="social" style="left:79px;background:#5cb4e0"></span>
  <span class="social" style="left:102px;background:#3b5998"></span>
  The contents of this site are copyright © 2012, Linden &amp; Crane. All Rights Reserved.
</footer>
</body>
</html>
```